New business! Essential Oils Label for 10 mL Essential Oils Bottles

I need a label design for my new essential oils business. The design should be easily transferable between products. Content should include:
label size W x H 1.25 x 2.875

LAVENDER
Lavandula angustifolia
VOLMIRAâ„¢
100% PURE ESSENTIAL OIL
Net 10 mL
For promotions and additional product information visit fb.com/VolmiraOils
VolmiraOils.com
Ashgrove, OR 33871
888-555-KIPO (5476)
Indications: Massage (10 drops of carrier oil for every drop of essential oil), Bath (10 drops of essential oil) or Inhalation (2-4 drops essential of on a tissue).
EXTERNAL USE ONLY- DILUTE BEFORE APPLICATION
Caution: Do not ingest the oil. Sensitive skin may be irritated by topical use. Avoid contact with eyes. Consult your healthcare practitioner before use. Store oil away from children and pets. Not meant for use during pregnancy. Seek medical care immediately if adverse reaction is experienced.

Target Market(s)

ONLINE SHOPPERS

Industry/Entity Type

Business

Font styles to use
Serif
Sans Serif

Colors

Designer to choose colors to be used in the design.

Requirements
Must have
• CONTENT AS LISTED IN PROJECT DESCRIPTION, LOGO (ATTACHED)
Nice to have
• Files with easily transferable content so the same label design can be used for multiple products.
Should not have
• Too small of print, difficult to read

```html
<!DOCTYPE html>
<html lang="en">
<head>
<meta charset="utf-8">
<title>Volmira Lavender Label</title>
<link href="https://fonts.googleapis.com/css2?family=Cinzel:wght@400;700&family=Josefin+Sans:wght@400&family=Open+Sans:wght@400&display=swap" rel="stylesheet">
<style>
  :root {
    --page: #e4e5e8;
    --violet: #6a629c;
    --lavender-ink: #5d56a8;
    --maroon: #6b1a1f;
    --blush: #f4a9a8;
    --white: #ffffff;
    --green: #1d8a42;
  }
  html, body { margin: 0; padding: 0; overflow: hidden; }
  body { width: 840px; height: 1200px; background: var(--page); position: relative; }
  .label {
    position: absolute; left: 0; top: 420px; width: 840px; height: 360px;
    background: var(--violet); overflow: hidden;
    font-family: "Open Sans", Arial, sans-serif; color: var(--white);
  }
  .panel { position: absolute; left: 0; top: 0; }
  .abs { position: absolute; margin: 0; }
  .name {
    left: 244px; width: 352px; top: 14px; text-align: center;
    font-family: "Cinzel", Georgia, serif; font-weight: 400; font-size: 33px; line-height: 34px;
    color: var(--lavender-ink); letter-spacing: 0.5px;
  }
  .latin {
    left: 244px; width: 352px; top: 48px; text-align: center;
    font-family: "Cinzel", Georgia, serif; font-size: 11.5px; line-height: 14px; color: var(--maroon);
    text-transform: uppercase; letter-spacing: 0.3px;
  }
  .brand-band { left: 264px; top: 76px; width: 312px; height: 64px; background: var(--blush); }
  .brand {
    left: 264px; width: 312px; top: 84px; text-align: center;
    font-family: "Josefin Sans", Arial, sans-serif; font-size: 50px; line-height: 52px;
    color: var(--maroon); letter-spacing: 3px;
  }
  .tm { left: 548px; top: 78px; font-size: 11px; color: var(--maroon); font-family: "Open Sans", Arial, sans-serif; }
  .sprig {
    left: 284px; top: 146px; width: 118px; height: 214px;
    background: linear-gradient(180deg, #b7a6d6 0%, #8a79b8 45%, #a8b88f 100%);
    border-radius: 6px; opacity: 0.85;
  }
  .purity { left: 426px; top: 156px; }
  .net {
    left: 420px; width: 110px; top: 320px; text-align: center;
    font-family: "Cinzel", Georgia, serif; font-weight: 700; font-size: 14px; color: var(--maroon);
  }
  .warning {
    left: 14px; width: 232px; top: 214px; text-align: center;
    font-family: "Cinzel", Georgia, serif; font-size: 17px; line-height: 18px;
  }
  .warning span { display: block; margin-bottom: 6px; }
  .contact {
    left: 14px; width: 232px; top: 302px; text-align: center;
    font-size: 13.5px; line-height: 20px;
  }
  .use-tag {
    right: 2px; height: 18px; background: var(--white); color: var(--maroon);
    font-family: "Cinzel", Georgia, serif; font-weight: 700; font-size: 15px; line-height: 19px;
    padding: 0 8px 0 10px;
  }
  .use-text {
    right: 18px; width: 230px; text-align: right; font-size: 13px; line-height: 20px;
  }
  .caution {
    left: 593px; width: 230px; top: 246px; text-align: justify; text-align-last: center;
    font-size: 10.2px; line-height: 13.2px;
  }
</style>
</head>
<body>
  <section class="label">
    <svg class="panel" width="840" height="360" viewBox="0 0 840 360" aria-hidden="true">
      <path d="M276 0 Q280 12 268 18 L268 168 Q246 176 244 200 Q246 224 268 232 L268 360 L572 360 L572 232 Q594 224 596 200 Q594 176 572 168 L572 18 Q560 12 564 0 Z" fill="var(--blush)"/>
      <path d="M288 0 Q290 16 278 24 L278 172 Q258 182 256 200 Q258 218 278 228 L278 360 L562 360 L562 228 Q582 218 584 200 Q582 182 562 172 L562 24 Q550 16 552 0 Z" fill="var(--white)"/>
    </svg>

    <h1 class="abs name">LAVENDER</h1>
    <p class="abs latin">Lavandula angustifolia</p>
    <div class="abs brand-band"></div>
    <p class="abs brand">VOLMIRA</p>
    <span class="abs tm">TM</span>

    <div class="abs sprig" role="img" aria-label="Photograph of lavender sprigs in bloom"></div>

    <svg class="abs purity" width="110" height="110" viewBox="0 0 110 110" aria-label="100% pure essential oil">
      <polygon points="55,6 98,30 98,80 55,104 12,80 12,30" fill="var(--green)"/>
      <polygon points="55,12 93,33 93,77 55,98 17,77 17,33" fill="none" stroke="var(--white)" stroke-width="1.5"/>
      <g transform="rotate(-18 55 55)" font-family="Cinzel, Georgia, serif" font-weight="700" fill="var(--white)" text-anchor="middle">
        <text x="55" y="48" font-size="12">100% PURE</text>
        <text x="55" y="62" font-size="12">ESSENTIAL</text>
        <text x="55" y="76" font-size="12">OIL</text>
      </g>
    </svg>

    <p class="abs net">NET 10 ML</p>

    <p class="abs warning"><span>EXTERNAL USE ONLY</span><span>DILUTE BEFORE<br>APPLICATION</span></p>
    <p class="abs contact">Ashgrove, OR 33871<br>888-555-KIPO (5476)</p>

    <span class="abs use-tag" style="top:40px">Massage</span>
    <p class="abs use-text" style="top:60px">(10 drops of carrier oil<br>for every drop of<br>essential oil),</p>
    <span class="abs use-tag" style="top:124px">Bath</span>
    <p class="abs use-text" style="top:144px">(10 drops of essential oil)</p>
    <span class="abs use-tag" style="top:168px">Inhalation</span>
    <p class="abs use-text" style="top:188px; right:10px; width:260px">(2-4 drops essential of on a tissue)</p>

    <p class="abs caution">Caution: Do not ingest the oil. Sensitive skin may be irritated by topical use. Avoid contact with eyes. Consult your healthcare practitioner before use. Store oil away from children and pets. Not meant for use during pregnancy. Seek medical care immediately if adverse reaction is experienced.</p>
  </section>
</body>
</html>
```